Upstart Retirement Planning Firm needs help with business card design

Harborlight Wealth Partners, LLC is looking for help with business card design. We give advice on investments, insurance, and other financial matters related to retirement. There are some required disclosures that we will provide but mostly we are looking for a professional, classy business card that reflects the theme we have chosen. We have a logo that is attached but we would like to add a phrase; "Shaping Your Working Savings Into Steady Comfort"

Doubled sided only so that we can add the required disclosures (needed for our industry) on the back of the card. We will provide the exact words for this in 1-2 days.

Target Market(s)

Retirees and Pre-retirees. Professionals 50+ years old

Industry/Entity Type

Financial Planning

Contact Information for Business Card

We currently have two people who will need separate cards so we'd like to have a template so that we can add names for new cards in the future.

For the first run, please show the following information.

Neil Osgood, MBA, ChFC®, CLU®
Financial Advisor, Registered Representative
nosgood@harborlightwp.example
Phone: (555) 218-3960
Toll Free Fax: (555) 218-3961

Address is
2876 Meadowbrook Pkwy.
Suite K418
Stonebridge Bay, OR 23019

Colors
3277b5

Requirements
Must have
• Logo, contact info, small phase to describe business (in description), required legal disclosures on back of the card as follows (in small font)
• Neil Osgood is a registered representative of and offers securities through Brightwater Capital Brokerage Corporation, Member SIPC. Brightwater Capital Brokerage Corporation is a member of the Brightwater Advisory Group which is the marketing name for Brightwater Holding Corporation and its affiliates.
Nice to have
• Rounded edges, raised letters
Should not have
• any colors that aren't in the logo (other than black for font)

```html
<!DOCTYPE html>
<html lang="en">
<head>
<meta charset="utf-8">
<title>Harborlight Wealth Partners — Business Card</title>
<link href="https://fonts.googleapis.com/css2?family=Arimo:wght@400;700&family=Marcellus+SC&display=swap" rel="stylesheet">
<style>
  :root {
    --backdrop: #e8e5e1;
    --card: #ffffff;
    --brand-blue: #0b4a9e;
    --ink: #1e1e1e;
    --ink-soft: #333333;
    --rule: #6d6d6d;
  }
  * { margin: 0; padding: 0; box-sizing: border-box; }
  html, body {
    width: 1200px;
    height: 1000px;
    overflow: hidden;
    background: var(--backdrop);
  }
  .canvas {
    position: relative;
    width: 1200px;
    height: 1000px;
  }
  .card {
    position: absolute;
    left: 293px;
    top: 322px;
    width: 612px;
    height: 358px;
    background: var(--card);
    border-radius: 16px;
    box-shadow: 0 4px 10px rgba(0,0,0,0.18);
    text-align: center;
    color: var(--ink);
    font-family: "Arimo", Arial, sans-serif;
  }
  .brand {
    position: absolute;
    left: 0;
    right: 0;
    top: 58px;
    font-family: "Marcellus SC", Georgia, serif;
    color: var(--brand-blue);
    font-weight: 400;
    line-height: 1.15;
  }
  .brand-name {
    font-size: 34px;
    letter-spacing: 0.5px;
  }
  .brand-suffix {
    font-size: 15px;
    letter-spacing: 4px;
    margin-top: 6px;
  }
  .tagline {
    position: absolute;
    left: 0;
    right: 0;
    top: 163px;
    font-family: "Marcellus SC", Georgia, serif;
    font-size: 17px;
    color: var(--ink-soft);
    letter-spacing: 0.3px;
  }
  .advisor-name {
    position: absolute;
    left: 0;
    right: 0;
    top: 205px;
    font-size: 17px;
    font-weight: 400;
    letter-spacing: 0.4px;
    text-transform: uppercase;
    color: #000;
  }
  .credentials,
  .role {
    position: absolute;
    left: 0;
    right: 0;
    font-size: 15.5px;
    color: var(--ink-soft);
  }
  .credentials { top: 233px; }
  .role { top: 253px; }
  .divider {
    position: absolute;
    left: 111px;
    width: 391px;
    top: 276px;
    height: 1px;
    background: var(--rule);
  }
  .contact {
    position: absolute;
    left: 0;
    right: 0;
    top: 283px;
    font-size: 15.5px;
    line-height: 19.5px;
    color: var(--ink);
    list-style: none;
  }
  .contact .sep { padding: 0 7px; }
</style>
</head>
<body>
  <main class="canvas">
    <article class="card" aria-label="Business card front">
      <header class="brand">
        <div class="brand-name">Harborlight Wealth Partners</div>
        <div class="brand-suffix">LLC</div>
      </header>

      <p class="tagline">Shaping Your Working Savings Into Steady Comfort</p>

      <h1 class="advisor-name">Neil Osgood</h1>
      <p class="credentials">MBA, ChFC®, CLU®</p>
      <p class="role">Financial Advisor, Registered Representative</p>

      <div class="divider"></div>

      <ul class="contact">
        <li>Email: nosgood@harborlightwp.example</li>
        <li>Phone: (555) 218-3960<span class="sep">|</span>Toll Free Fax: (555) 218-3961</li>
        <li>2876 Meadowbrook Pkwy., Suite K418, Stonebridge Bay, OR 23019</li>
      </ul>
    </article>
  </main>
</body>
</html>
```